Maple Lodging Hub website, brand new company, that rents rooms out in houses to milleniuls

We have a site right now that is weak as heck! We could use some punching it up. So we want it to be fun and cool, with added items in for social media (just twitter now) and anything else you want to throw at us. We do have a “blog” in there dedicated to events (we throw a lot of them) so want to incorporate that. Also have an existing design for a hand out that we want to use as our launching pad for colors… you can deviate from it a bit though.

Target Market(s)

25-40 year olds transitioning to the city from other places in the country. Millennial are the min group

Industry/Entity Type

Real Estate

Coding

Coded - Design and coding required

Number of Pages Required

5+ page

Font styles to use
Sans Serif

Requirements
Must have
• Fun look, same pages as those uploaded, but not necessarily the look and feel of what we have already.
• Follow the content of our posted site www.MapleLodgingHub.example
• FOOTER
• LOGO | SITEMAP | SOCIAL LINKS | MAIN CTA REMINDER | CONTACT INFO | COPYRIGHT INFO | TERMS AND CONDITIONS
Nice to have
• Use as many of my graphics as loaded, but feel free to use stock photos as well interlaced. Including both people in their 20’s, 30’s, 40’s, having a fun time or of nice houses, inside and out.

```html
<!DOCTYPE html>
<html lang="en">
<head>
<meta charset="utf-8">
<title>Maple Lodging Hub</title>
<link rel="stylesheet" href="https://fonts.googleapis.com/css2?family=Cabin:wght@400;500;600;700&family=Open+Sans:wght@400;600;700&display=swap">
<style>
:root{
  --blue:#1756aa;
  --blue-dark:#124a94;
  --green:#6aab24;
  --green-dark:#5b9a1c;
  --grey-bg:#e5e5e5;
  --grey-card:#ececec;
  --fans-bg:#e9e9e9;
  --ink:#2a2a2a;
  --text:#333;
  --white:#fff;
  --footer:#1b1b1b;
}
*{box-sizing:border-box;margin:0;padding:0}
html,body{width:1200px;height:2757px;overflow:hidden}
body{position:relative;background:var(--grey-bg);font-family:"Open Sans",Arial,sans-serif;color:var(--text)}
.abs{position:absolute}

/* nav */
.main-nav{left:0;top:0;width:1200px;height:48px;background:var(--green)}
.main-nav a{position:absolute;top:15px;color:var(--white);font:600 14px/1 "Open Sans",sans-serif;text-decoration:none;letter-spacing:.3px}

/* hero */
.hero{left:0;top:48px;width:1200px;height:415px;background:var(--blue);overflow:hidden}
.hero-photo{left:430px;top:0;width:770px;height:415px}
.brand{left:100px;top:190px;width:400px;text-align:center;color:var(--green);font:700 42px/1.05 "Cabin",sans-serif;letter-spacing:1px;text-transform:uppercase}
.brand-mark{display:block;width:26px;height:26px;background:var(--green);margin:0 auto 14px}

.hero-wave{left:0;top:360px;width:1200px;height:110px}

/* content panel */
.content-panel{left:77px;top:440px;width:1048px;height:1144px;background:var(--white)}
.tagline{font:400 27px/1 "Cabin",sans-serif;color:var(--ink);letter-spacing:.3px;text-transform:uppercase}
.tagline-one{left:121px;top:483px}
.tagline-two{left:610px;top:535px}
.tagline-cross-v{left:598px;top:476px;width:2px;height:92px;background:var(--blue)}
.tagline-cross-h{left:555px;top:522px;width:88px;height:2px;background:var(--blue)}

.feature{top:634px;height:404px;color:var(--white);padding:34px 40px 0 21px}
.feature-blue{left:97px;width:502px;background:var(--blue);padding-right:62px}
.feature-green{left:599px;width:504px;background:var(--green);padding-left:55px}
.feature h2{font:500 26px/1 "Cabin",sans-serif;text-transform:uppercase;letter-spacing:.4px;margin-bottom:22px}
.feature p{font-size:14.5px;line-height:27px;margin:0 0 22px 0}
.feature ul{list-style:none}
.feature li{font-size:14.5px;line-height:20px;margin-bottom:9px;padding-left:20px;position:relative}
.feature li::before{content:"";position:absolute;left:0;top:6px;width:8px;height:8px;border-top:2px solid var(--white);border-right:2px solid var(--white);transform:rotate(45deg)}
.contact-badge{left:560px;top:777px;width:74px;height:74px;border-radius:50%;background:var(--white);color:var(--ink);font:600 13px/15px "Open Sans",sans-serif;text-align:center;padding-top:22px;box-shadow:0 0 0 3px rgba(0,0,0,.08)}

.card{top:1121px;width:299px;height:344px;background:var(--grey-card);border-bottom:4px solid var(--blue);text-align:center}
.card-one{left:103px}
.card-two{left:448px;background:var(--white);border:2px solid #cfcfcf;border-bottom:4px solid var(--green)}
.card-three{left:792px}
.card h3{font:600 20px/1 "Cabin",sans-serif;color:var(--ink);text-transform:uppercase;margin-top:17px;letter-spacing:.3px}
.card-two h3{color:var(--green)}
.card-photo{display:block;margin:16px auto 0;width:262px;height:130px}
.card p{font-size:13px;line-height:22px;margin:20px 12px 0;color:var(--ink)}
.card a{display:block;margin-top:12px;font:700 13.5px/1 "Open Sans",sans-serif;color:var(--blue);text-decoration:none;letter-spacing:.5px}
.card-two a{color:var(--green)}

/* gallery */
.gallery{left:0;top:1557px;width:1200px;height:489px;background:var(--blue)}
.section-title{position:absolute;left:0;width:1200px;text-align:center;font:600 30px/1 "Cabin",sans-serif;letter-spacing:1px}
.section-rule{position:absolute;height:1px}
.gallery .section-title{top:106px;color:var(--white)}
.gallery .section-rule{top:122px;background:rgba(255,255,255,.3)}
.gallery-svg{left:0;top:0;width:1200px;height:489px}

/* fans */
.fans{left:0;top:2046px;width:1200px;height:413px;background:var(--fans-bg)}
.fans-inner{left:10px;top:0;width:1176px;height:413px;background:#ececec}
.fans .section-title{top:40px;color:var(--blue)}
.fans .section-rule{top:55px;background:#c9c9c9}
.quote{left:305px;top:108px;width:600px;text-align:center;font:400 16px/22px Arial,Helvetica,sans-serif;color:#444}
.quote-mark{left:280px;top:106px;font:700 26px/1 Georgia,serif;color:#444}
.quote-by{left:0;top:2261px;width:1200px;text-align:center;font:italic 12px/1 Arial,sans-serif;color:#888}
.fans-svg{left:0;top:0;width:1200px;height:413px}

/* footer */
.site-footer{left:0;top:2459px;width:1200px;height:298px;background:var(--footer);text-align:center}
.footer-brand{left:0;top:45px;width:1200px;color:var(--blue);font:700 26px/1.05 "Cabin",sans-serif;text-transform:uppercase;letter-spacing:1px}
.footer-nav{left:0;top:138px;width:1200px;font-size:12.5px;color:var(--white);letter-spacing:.3px}
.footer-nav a{color:var(--white);text-decoration:none}
.footer-nav span{margin:0 18px}
.copyright{left:0;top:173px;width:1200px;font-size:13px;color:var(--white)}
.social{top:215px;width:26px;height:26px;background:#3a3a3a;border-radius:2px}
.social-active{background:#1d9fe0}
</style>
</head>
<body>

<nav class="main-nav abs">
  <a style="left:110px">WELCOME</a>
  <a style="left:222px">OUR COMMUNITIES</a>
  <a style="left:393px">AMMENITIES</a>
  <a style="left:520px">FITTING</a>
  <a style="left:617px">EVENTS</a>
  <a style="left:713px">ABOUT US</a>
  <a style="left:823px">CONTACT</a>
</nav>

<header class="hero abs">
  <svg class="hero-photo abs" viewBox="0 0 770 415" role="img" aria-label="Photo of a brick house with a white garage, green lawn and trees">
    <defs>
      <linearGradient id="sky" x1="0" y1="0" x2="0" y2="1">
        <stop offset="0" stop-color="#c9d6e2"/>
        <stop offset=".45" stop-color="#8a7a6a"/>
        <stop offset=".7" stop-color="#c7c2b8"/>
        <stop offset="1" stop-color="#5f8c2f"/>
      </linearGradient>
      <linearGradient id="fade" x1="0" y1="0" x2="1" y2="0">
        <stop offset="0" stop-color="#1756aa" stop-opacity="1"/>
        <stop offset=".35" stop-color="#1756aa" stop-opacity="0"/>
      </linearGradient>
    </defs>
    <rect width="770" height="415" fill="url(#sky)"/>
    <rect width="770" height="415" fill="url(#fade)"/>
  </svg>
  <div class="brand abs"><span class="brand-mark"></span>Maple Lodging Hub</div>
</header>

<div class="content-panel abs"></div>
<svg class="hero-wave abs" viewBox="0 0 1200 110" aria-hidden="true">
  <path d="M77 60 C 250 25, 420 28, 600 40 S 950 55, 1125 52 L1125 110 L77 110 Z" fill="#fff"/>
  <path d="M77 60 C 250 25, 420 28, 600 40 S 950 55, 1125 52" fill="none" stroke="#6aab24" stroke-width="5"/>
</svg>

<div class="tagline tagline-one abs">Professional Built Communities</div>
<div class="tagline tagline-two abs">Community Built Professionals</div>
<div class="tagline-cross-v abs"></div>
<div class="tagline-cross-h abs"></div>

<section class="feature feature-blue abs">
  <h2>Experience the Difference</h2>
  <p>Traditional apartments and housing rentals are a thing of the past. We have created an all-encompassing living experience that aligns perfectly with your trendy, yet sophisticated lifestyle. Maple Lodging Hub is unlike anything you have ever experienced before.</p>
  <p>We invite you to explore our selection of home communities and discover the passion we have for providing wonderful experiences.</p>
</section>
<section class="feature feature-green abs">
  <h2>Luxurious Amenities*</h2>
  <ul>
    <li>High-speed Wi-Fi</li>
    <li>All inclusive utilities (with Green Cap)</li>
    <li>Optional enclosed garage</li>
    <li>Fully furnished kitchen</li>
    <li>Washer and dryer</li>
    <li>Spacious, newly updated rooms</li>
    <li>Private use, full bath with each room</li>
    <li>Bi-monthly community events</li>
    <li>Various networking event invitations, well suited for young professionals</li>
  </ul>
</section>
<div class="contact-badge abs">CONTACT<br>US</div>

<article class="card card-one abs">
  <h3>@ Home with MLH</h3>
  <svg class="card-photo" viewBox="0 0 262 130" role="img" aria-label="Photo of young friends smiling together at a pub"><rect width="262" height="130" fill="#5a3a34"/><rect width="262" height="130" fill="#c0392b" opacity=".25"/></svg>
  <p>After an exhausting day in the office, the thought of hanging out with co workers is the last thing on your mind. But who says you have to conquer a crowded pub...</p>
  <a>READ MORE</a>
</article>
<article class="card card-two abs">
  <h3>Most Recent Events</h3>
  <svg class="card-photo" viewBox="0 0 262 130" role="img" aria-label="Photo of a group of friends at an event in a bar"><rect width="262" height="130" fill="#4a4642"/><rect width="262" height="130" fill="#d9a441" opacity=".2"/></svg>
  <p>After an exhausting day in the office, the thought of hanging out with co workers is the last thing on your mind. But who says you have to conquer a crowded pub...</p>
  <a>READ MORE</a>
</article>
<article class="card card-three abs">
  <h3>Our Latest Addition</h3>
  <svg class="card-photo" viewBox="0 0 262 130" role="img" aria-label="Photo of young friends smiling together at a pub"><rect width="262" height="130" fill="#5a3a34"/><rect width="262" height="130" fill="#c0392b" opacity=".25"/></svg>
  <p>After an exhausting day in the office, the thought of hanging out with co workers is the last thing on your mind. But who says you have to conquer a crowded pub...</p>
  <a>READ MORE</a>
</article>

<section class="gallery abs">
  <div class="section-rule" style="left:258px;width:240px"></div>
  <div class="section-rule" style="left:702px;width:240px"></div>
  <h2 class="section-title">GALLERY</h2>
  <svg class="gallery-svg abs" viewBox="0 0 1200 489">
    <circle cx="182" cy="301" r="72" fill="#a5452a" role="img" aria-label="Photo of a wooden kitchen"/>
    <circle cx="345" cy="301" r="72" fill="#5a5350" role="img" aria-label="Photo of a dining room with table and chairs"/>
    <circle cx="849" cy="301" r="72" fill="#bfc0bd" role="img" aria-label="Photo of a white kitchen with steel appliances"/>
    <circle cx="1013" cy="301" r="72" fill="#7b95a8" role="img" aria-label="Photo of a house exterior with a front porch"/>
    <circle cx="597" cy="301" r="120" fill="#8c7a68" stroke="#6aab24" stroke-width="7" role="img" aria-label="Photo of a living room with an armchair, rug and glass table"/>
    <path d="M460 289 L448 301 L460 313" fill="none" stroke="#fff" stroke-width="4"/>
    <path d="M737 289 L749 301 L737 313" fill="none" stroke="#fff" stroke-width="4"/>
    <circle cx="679" cy="395" r="20" fill="#fff"/>
    <circle cx="679" cy="395" r="15" fill="#1756aa"/>
    <path d="M679 387 V403 M671 395 H687" stroke="#fff" stroke-width="3"/>
  </svg>
</section>

<section class="fans abs">
  <div class="fans-inner abs"></div>
  <div class="section-rule" style="left:254px;width:250px"></div>
  <div class="section-rule" style="left:696px;width:250px"></div>
  <h2 class="section-title">OUR FANS</h2>
  <div class="quote-mark abs">&ldquo;</div>
  <p class="quote abs">Lorem ipsum dolor sit amet, consectetur adipiscing elit, sed do eiusmod tempor incididunt ut labore et dolore magna aliqua. Ut enim ad minim veniam, quis nostrud exercitation ullamco laboris nisi ut aliquip ex ea commodo consequat. Duis aute irure dolor in reprehenderit in voluptate velit esse cillum dolore eu fugiat nulla pariatur.</p>
  <svg class="fans-svg abs" viewBox="0 0 1200 413">
    <path d="M129 136 L119 147 L129 158" fill="none" stroke="#bbb" stroke-width="5"/>
    <path d="M1050 136 L1060 147 L1050 158" fill="none" stroke="#bbb" stroke-width="5"/>
    <circle cx="500" cy="329" r="20" fill="#d8d2cc" stroke="#ddd" stroke-width="3" role="img" aria-label="Small portrait of a fan"/>
    <circle cx="678" cy="329" r="20" fill="#e0d6c8" stroke="#ddd" stroke-width="3" role="img" aria-label="Small portrait of a fan"/>
    <circle cx="590" cy="297" r="53" fill="#6d8f5a" stroke="#6aab24" stroke-width="5" role="img" aria-label="Portrait of a featured fan"/>
  </svg>
</section>
<div class="quote-by abs">&mdash; Someone famous</div>

<footer class="site-footer abs">
  <div class="footer-brand abs">Maple Lodging Hub</div>
  <div class="footer-nav abs"><a>WELCOME</a><span>|</span><a>OUR COMMUNITIES</a><span>|</span><a>AMMENITIES</a><span>|</span><a>FITTING</a><span>|</span><a>EVENTS</a><span>|</span><a>ABOUT US</a><span>|</span><a>CONTACT</a></div>
  <div class="copyright abs">Copyright &copy; 2016 Maple Lodging Hub. Right Reserved.</div>
  <a class="social abs" style="left:520px" aria-label="Social link"></a>
  <a class="social social-active abs" style="left:560px" aria-label="Social link"></a>
  <a class="social abs" style="left:601px" aria-label="Social link"></a>
  <a class="social abs" style="left:641px" aria-label="Social link"></a>
</footer>

</body>
</html>
```